Tessa Lane Staging & Design - a company built on first impressions, needs an impressive letterhead

Please create a letter head to be used for our project proposals, contract agreements and other client correspondence. We are a home Staging and interior design company. We like sleek, modern, clean and elegant design. Please create a document that compliments and uses our logo. We will also be creating flyers that we would like to match our letterhead and future marketing materials

Target Market(s)

real estate agents, home owners looking to sell

Industry/Entity Type

Interior Design

```html
<!DOCTYPE html>
<html lang="en">
<head>
<meta charset="UTF-8">
<title>Tessa Lane Staging &amp; Design — Letterhead</title>
<link href="https://fonts.googleapis.com/css2?family=Montserrat:wght@300&display=swap" rel="stylesheet">
<style>
  :root {
    --paper: #ffffff;
    --ink: #2b2b2b;
    --rule-dark: #5a5a5a;
    --rule-light: #d4d4d4;
    --mark-faint: #e6e7e8;
  }
  html, body {
    margin: 0;
    padding: 0;
    overflow: hidden;
    background: var(--paper);
  }
  .letterhead {
    position: relative;
    width: 927px;
    height: 1200px;
    background: var(--paper);
    overflow: hidden;
    font-family: "Montserrat", sans-serif;
    font-weight: 300;
    color: var(--ink);
  }
  .brand-name {
    position: absolute;
    right: 41px;
    top: 74px;
    margin: 0;
    font-size: 24px;
    font-weight: 300;
    letter-spacing: 0.14em;
    text-transform: uppercase;
    color: var(--ink);
  }
  .header-rule {
    position: absolute;
    left: 76px;
    top: 132px;
    width: 810px;
    height: 1px;
    background: linear-gradient(to right, rgba(90,90,90,0), var(--rule-dark) 8%);
  }
  .brand-tagline {
    position: absolute;
    right: 41px;
    top: 143px;
    margin: 0;
    font-size: 17px;
    font-weight: 300;
    letter-spacing: 0.12em;
    text-transform: uppercase;
    color: var(--ink);
  }
  .backdrop-name {
    position: absolute;
    left: 0;
    right: 0;
    top: 548px;
    margin: 0;
    text-align: center;
    font-size: 86px;
    font-weight: 300;
    letter-spacing: 0.08em;
    text-transform: uppercase;
    color: var(--mark-faint);
  }
  .footer-rule {
    position: absolute;
    left: 0;
    top: 1120px;
    width: 927px;
    height: 1px;
    background: var(--rule-light);
  }
</style>
</head>
<body>
  <main class="letterhead">
    <header>
      <p class="brand-name">Tessa Lane</p>
      <div class="header-rule"></div>
      <p class="brand-tagline">Staging &amp; Design</p>
    </header>
    <p class="backdrop-name" aria-hidden="true">Tessa Lane</p>
    <footer>
      <div class="footer-rule"></div>
    </footer>
  </main>
</body>
</html>
```